Building / construction Bussiness card design

I need a new design and logo for my company LWT I am a builder who can project manage or design and construct any kind of building, Residential, Commercial and industrial construction.

On the face side of the card I would like to have just the logo.

Industry/Entity Type

Construction

Contact Information for Business Card

LWT Lakeside Works Team
ABN:84 392 017 655
Carl Moretti
Licenced Builders
0471 926 054
carl@lakesideworksteam.com.au
PO Box 482 Tallowmere BC 2739

```html
<!DOCTYPE html>
<html lang="en">
<head>
<meta charset="utf-8">
<title>LWT Lakeside Works Team – Business Card</title>
<link rel="stylesheet" href="https://fonts.googleapis.com/css2?family=Roboto+Condensed:ital,wght@0,400;1,300&display=swap">
<style>
  :root {
    --page-bg: #ffffff;
    --ink: #111111;
    --email-red: #e8141a;
    --grad-yellow: #f7f74a;
    --grad-lime: #b8f52a;
    --grad-green: #4dff10;
    --grad-teal: #218a66;
    --grad-blue: #0a1fe6;
    --card-edge: #1c7a55;
    --shadow: rgba(0, 0, 0, 0.95);
  }

  * { margin: 0; padding: 0; box-sizing: border-box; }

  html, body {
    width: 1200px;
    height: 900px;
    overflow: hidden;
    background: var(--page-bg);
  }

  .canvas {
    position: relative;
    width: 1200px;
    height: 900px;
    overflow: hidden;
  }

  .card {
    position: absolute;
    background: linear-gradient(90deg,
      var(--grad-yellow) 0%,
      var(--grad-lime) 30%,
      var(--grad-green) 58%,
      var(--grad-green) 66%,
      var(--grad-teal) 86%,
      var(--grad-blue) 98%);
  }

  .card--front {
    left: 28px;
    top: 55px;
    width: 542px;
    height: 693px;
    border-radius: 46px / 70px;
    border: 1.5px solid var(--card-edge);
    box-shadow: 28px 40px 30px var(--shadow);
  }

  .card--back {
    left: 657px;
    top: 58px;
    width: 543px;
    height: 688px;
    border-radius: 40px / 90px;
  }

  .brand-name {
    position: absolute;
    left: -16px;
    width: 100%;
    text-align: center;
    font-family: "Roboto Condensed", sans-serif;
    font-weight: 400;
    font-style: normal;
    color: var(--ink);
    line-height: 1;
    white-space: nowrap;
  }

  .brand-name__initials {
    top: 150px;
    font-size: 200px;
  }

  .brand-name__full {
    top: 382px;
    font-size: 40px;
  }

  .contact {
    position: absolute;
    font-family: "Roboto Condensed", sans-serif;
    color: var(--ink);
    text-align: center;
    white-space: nowrap;
    line-height: 1;
  }

  .contact__name {
    left: 200px;
    top: 140px;
    width: 270px;
    font-style: italic;
    font-weight: 300;
    font-size: 38px;
  }

  .contact__role {
    left: 200px;
    top: 196px;
    width: 270px;
    font-size: 34px;
  }

  .contact__line {
    left: 0;
    width: 540px;
    font-size: 31px;
  }

  .contact__mobile { top: 365px; left: 10px; }
  .contact__postal { top: 462px; left: 2px; }
  .contact__abn { top: 514px; left: -4px; }

  .contact__email {
    top: 418px;
    left: 0;
    width: 540px;
    font-size: 25px;
    color: var(--email-red);
  }
</style>
</head>
<body>
  <main class="canvas">
    <section class="card card--front" aria-label="Card front">
      <div class="brand-name brand-name__initials">LWT</div>
      <div class="brand-name brand-name__full">Lakeside Works Team</div>
    </section>

    <section class="card card--back" aria-label="Card back">
      <p class="contact contact__name">CARL&nbsp;&nbsp;MORETTI</p>
      <p class="contact contact__role">Licensed Builders</p>
      <p class="contact contact__line contact__mobile">Mobile #&nbsp;&nbsp;0471 926 054</p>
      <p class="contact contact__email">email: carl@lakesideworksteam.com.au</p>
      <p class="contact contact__line contact__postal">PO Box 482&nbsp;&nbsp;Tallowmere, BC 2739</p>
      <p class="contact contact__line contact__abn">ABN&nbsp;&nbsp;84 392 017 655</p>
    </section>
  </main>
</body>
</html>
```